Pinewick Capital Partners - Company Envelopes

I am looking for a graphic designer to create a bespoke envelope for my company use, which I can then have printed at scale. The envelope should be of standard size and shape, but Matt black in colour, with semi-thick vertical gloss (shiny) lines going from left to right, but must stop to the right of the envelope, leaving a Matt black line with enough space for a stamp in the top right corner. The back of the envelope should be full Matt black.

Requirements
Must have
• Must be as described in brief
Should not have
• No other colours - Just Matt and Gloss Black

```html
<!DOCTYPE html>
<html lang="en">
<head>
<meta charset="utf-8">
<title>Pinewick Capital Partners – Company Envelopes</title>
<link rel="stylesheet" href="https://fonts.googleapis.com/css2?family=Playfair+Display:wght@600&display=swap">
<style>
  :root {
    --backdrop: #5e5e5e;
    --matt-black: #0b0b0b;
    --matt-black-soft: #141414;
    --gloss-black: #000000;
    --gloss-sheen: #b9b9b9;
    --stamp-area: #1d1d1d;
    --flap-line: #d6d6d6;
    --wordmark: #ececec;
  }
  * { margin: 0; padding: 0; box-sizing: border-box; }
  html, body {
    width: 1200px; height: 895px; overflow: hidden;
    background: var(--backdrop);
  }
  .canvas { position: relative; width: 1200px; height: 895px; }

  .envelope {
    position: absolute;
    left: 365px;
    width: 471px;
    height: 333px;
    background:
      radial-gradient(ellipse at 40% 30%, var(--matt-black-soft), var(--matt-black) 70%);
    overflow: hidden;
  }
  .envelope--back { top: 92px; }
  .envelope--front { top: 469px; }

  .flap-outline { position: absolute; left: 0; top: 0; }

  .gloss-stripe {
    position: absolute;
    top: 0;
    width: 31.4px;
    background: var(--gloss-black);
  }
  .gloss-stripe--short { height: 183.6px; }
  .gloss-stripe--long { height: 333px; }
  .gloss-stripe--sheen-1 {
    background: linear-gradient(170deg, var(--gloss-black) 38%, #6a6a6a 65%, var(--gloss-sheen) 100%);
  }
  .gloss-stripe--sheen-2 {
    background: linear-gradient(168deg, var(--gloss-black) 28%, #8a8a8a 55%, var(--gloss-sheen) 80%);
  }
  .gloss-stripe--sheen-3 {
    background: linear-gradient(166deg, var(--gloss-black) 18%, #8f8f8f 48%, var(--gloss-sheen) 72%);
  }

  .stamp-area {
    position: absolute;
    left: 317px;
    top: 33px;
    width: 126px;
    height: 126px;
    background: var(--stamp-area);
  }

  .wordmark {
    position: absolute;
    left: 16px;
    top: 199px;
    width: 150px;
    color: var(--wordmark);
    font-family: "Playfair Display", Georgia, serif;
    font-weight: 600;
    text-align: left;
    line-height: 1;
  }
  .wordmark__name { display: block; font-size: 22px; letter-spacing: 0.5px; }
  .wordmark__tagline { display: block; font-size: 6.4px; letter-spacing: 2.2px; margin-top: 3px; }
</style>
</head>
<body>
<main class="canvas">

  <section class="envelope envelope--back" aria-label="Envelope back">
    <svg class="flap-outline" width="471" height="333" viewBox="0 0 471 333">
      <path d="M0.5 0.5 L14.6 56 Q21 75 39 75 L432 75 Q450 75 456.4 56 L470.5 0.5 L0.5 0.5"
            fill="none" stroke="var(--flap-line)" stroke-width="0.8"/>
    </svg>
  </section>

  <section class="envelope envelope--front" aria-label="Envelope front">
    <div class="gloss-stripe gloss-stripe--short" style="left:0"></div>
    <div class="gloss-stripe gloss-stripe--short" style="left:43.9px"></div>
    <div class="gloss-stripe gloss-stripe--short" style="left:87.7px"></div>
    <div class="gloss-stripe gloss-stripe--short" style="left:131.6px"></div>
    <div class="gloss-stripe gloss-stripe--long gloss-stripe--sheen-1" style="left:175.4px"></div>
    <div class="gloss-stripe gloss-stripe--long gloss-stripe--sheen-2" style="left:219.3px"></div>
    <div class="gloss-stripe gloss-stripe--long gloss-stripe--sheen-3" style="left:263.2px"></div>

    <div class="stamp-area" aria-label="Stamp area"></div>

    <p class="wordmark">
      <span class="wordmark__name">PINEWICK</span>
      <span class="wordmark__tagline">CAPITAL PARTNERS</span>
    </p>
  </section>

</main>
</body>
</html>
```